Smoked and Dried Fish Business Cards

We need a business card design for a new company called The Copperwake Limited. We import smoked and dried fish from Ghana and distribute worldwide. We would like to see designs that use colours red yellow and green. The final design should communicate healthy and saftey food environment.

Industry/Entity Type

Business

Contact Information for Business Card

The Copperwake Limited.
87 Brindle Row. Hollin Vale.
London.
SE14 3QJ.
TEL: 01632 960417. Mobile. 07700 900318 /07700900562
Website: www.copperwakeltd.com email: sales@copperwakeltd.com

```html
<!DOCTYPE html>
<html lang="en">
<head>
<meta charset="utf-8">
<title>The Copperwake Limited – Business Card</title>
<link rel="stylesheet" href="https://fonts.googleapis.com/css2?family=Tinos:wght@700&family=PT+Sans:wght@400;700&display=swap">
<style>
  :root {
    --page-bg: #2b2b2b;
    --card-white: #ffffff;
    --card-fade: #e9e9e9;
    --brand-green: #0f8a45;
    --brand-yellow: #f2c11a;
    --brand-red: #c8161d;
    --ink: #1a1a1a;
    --art-grey: #cfcfcf;
    --art-pale: #ececec;
  }
  * { margin: 0; padding: 0; box-sizing: border-box; }
  html, body { width: 1200px; height: 900px; overflow: hidden; }
  body {
    background: var(--page-bg);
    display: flex;
    align-items: center;
    justify-content: center;
  }
  .business-card {
    position: relative;
    width: 1000px;
    height: 571px;
    background: linear-gradient(160deg, var(--card-white) 40%, var(--card-fade) 100%);
    overflow: hidden;
  }
  .header-band {
    position: absolute;
    left: 0; top: 0;
    width: 100%;
    height: 104px;
    background: var(--brand-green);
  }
  .company-name {
    position: absolute;
    left: 42px;
    top: 30px;
    font-family: "Tinos", "Times New Roman", serif;
    font-weight: 700;
    font-size: 42px;
    color: var(--card-white);
    letter-spacing: 0.5px;
  }
  .stripe-yellow {
    position: absolute;
    left: 0; top: 104px;
    width: 100%; height: 9px;
    background: var(--brand-yellow);
  }
  .stripe-red {
    position: absolute;
    left: 0; top: 113px;
    width: 100%; height: 8px;
    background: var(--brand-red);
  }
  .fish-artwork {
    position: absolute;
    right: 0;
    top: 121px;
    width: 470px;
    height: 450px;
    background:
      radial-gradient(ellipse at 72% 62%, var(--art-grey) 0%, var(--art-pale) 55%, transparent 80%);
  }
  .contact-block {
    position: absolute;
    left: 52px;
    top: 170px;
    font-family: "PT Sans", "Myriad Pro", sans-serif;
    color: var(--ink);
    font-size: 25px;
    line-height: 36px;
  }
  .contact-address { margin-bottom: 0; }
  .contact-row { display: flex; }
  .contact-label {
    width: 138px;
    font-weight: 700;
    font-size: 27px;
  }
  .contact-value::before { content: ": "; }
</style>
</head>
<body>
  <div class="business-card">
    <div class="header-band"></div>
    <h1 class="company-name">The Copperwake Limited</h1>
    <div class="stripe-yellow"></div>
    <div class="stripe-red"></div>

    <div class="fish-artwork" role="img" aria-label="Decorative area for fish illustration in grey with red, yellow and green accents"></div>

    <div class="contact-block">
      <p class="contact-address">87&nbsp; Brindle Row. Hollin Vale. London. SE14 3QJ</p>
      <p class="contact-row"><span class="contact-label">Tel</span><span class="contact-value">01632 960417</span></p>
      <p class="contact-row"><span class="contact-label">Mobile</span><span class="contact-value">07700 900318 /07700900562</span></p>
      <p class="contact-row"><span class="contact-label">Website</span><span class="contact-value">www.copperwakeltd.com</span></p>
      <p class="contact-row"><span class="contact-label">Email</span><span class="contact-value">sales@copperwakeltd.com</span></p>
    </div>
  </div>
</body>
</html>
```